Vex Pim ORA Need a custom graphic

I need to have the attached chart re-designed in a hand colored pencil format. The heading needs to be changed to "The most effective methods for hiring sales people". Do not include the background logo in the sample file.

Place the attached Vex Pim ORA logo next to the most effective methods (91%)

```html
<!DOCTYPE html>
<html lang="en">
<head>
<meta charset="utf-8">
<title>The Most Effective Methods for Hiring Sales People</title>
<link href="https://fonts.googleapis.com/css2?family=Exo+2:ital,wght@0,700;0,800;1,700;1,800&family=Montserrat:wght@800&display=swap" rel="stylesheet">
<style>
  :root {
    --page: #ffffff;
    --panel: #e6e6e7;
    --brand-green: #5cb82a;
    --tag-green: #6cc01f;
    --ink: #3a3a3c;
    --white: #ffffff;
    --bar-1: #5a5ec6;
    --bar-2: #3f7cc8;
    --bar-3: #2a95c6;
    --bar-4: #3aaec2;
    --bar-5: #1dbdae;
    --bar-6: #2bb39a;
    --bar-7: #1e8c4c;
    --bar-8: #4b9b3b;
    --bar-9: #68aa38;
    --bar-10: #7bb63a;
    --bar-11: #8a8e6c;
    --link-start: #5fbe3b;
    --link-end: #16bfb2;
  }
  html, body {
    margin: 0;
    padding: 0;
    width: 1200px;
    height: 901px;
    overflow: hidden;
    background: var(--page);
  }
  .chart {
    display: block;
    width: 1200px;
    height: 901px;
  }
  .title-band { fill: var(--brand-green); }
  .title {
    font-family: "Montserrat", sans-serif;
    font-weight: 800;
    font-size: 23px;
    letter-spacing: 0.6px;
    fill: var(--ink);
  }
  .panel { fill: var(--panel); }
  .axis-band { fill: var(--brand-green); }
  .axis-tick { fill: var(--ink); }
  .axis-title {
    font-family: "Exo 2", sans-serif;
    font-style: italic;
    font-weight: 800;
    font-size: 22px;
    letter-spacing: 2px;
    fill: var(--ink);
  }
  .axis-label {
    font-family: "Exo 2", sans-serif;
    font-style: italic;
    font-weight: 800;
    font-size: 14px;
    letter-spacing: 1px;
    fill: var(--ink);
  }
  .bar-label {
    font-family: "Exo 2", sans-serif;
    font-style: italic;
    font-weight: 800;
    fill: var(--white);
    letter-spacing: 0.8px;
  }
  .bar-label--lg { font-size: 10.5px; }
  .bar-label--sm { font-size: 6.5px; letter-spacing: 0.5px; }
  .tag { fill: var(--tag-green); }
  .tag-text {
    font-family: "Exo 2", sans-serif;
    font-style: italic;
    font-weight: 800;
    fill: var(--white);
  }
  .tag-text--lg { font-size: 8px; }
  .tag-text--sm { font-size: 6px; }
  .client-name {
    font-family: "Montserrat", sans-serif;
    font-weight: 800;
    font-size: 15px;
    letter-spacing: 0.5px;
    fill: var(--ink);
  }
  .footer-band { fill: var(--brand-green); }
  .footer-title {
    font-family: "Montserrat", sans-serif;
    font-weight: 800;
    font-size: 22px;
    letter-spacing: 3px;
    fill: var(--ink);
  }
</style>
</head>
<body>
<svg class="chart" viewBox="0 0 945 712" preserveAspectRatio="none" xmlns="http://www.w3.org/2000/svg" role="img" aria-label="Bar chart: the most effective methods for hiring sales people by predictive validity">
  <defs>
    <linearGradient id="link-fill" x1="0" y1="0" x2="1" y2="0">
      <stop offset="0" stop-color="var(--link-start)"/>
      <stop offset="1" stop-color="var(--link-end)"/>
    </linearGradient>
  </defs>

  <!-- heading -->
  <rect class="title-band" x="48" y="83" width="850" height="53"/>
  <text class="title" x="473" y="118" text-anchor="middle">THE MOST EFFECTIVE METHODS FOR HIRING SALES PEOPLE</text>

  <!-- chart panel -->
  <rect class="panel" x="48" y="150" width="850" height="477"/>

  <!-- vertical axis -->
  <rect class="axis-band" x="72" y="165" width="28" height="442"/>
  <rect class="axis-tick" x="84" y="180" width="4" height="20"/>
  <rect class="axis-tick" x="84" y="574" width="4" height="20"/>
  <text class="axis-title" transform="translate(95 387) rotate(-90)" text-anchor="middle">PREDICTIVE VALIDITY</text>

  <g class="axis-labels">
    <text class="axis-label" x="108" y="191">0.90</text>
    <text class="axis-label" x="108" y="236">0.80</text>
    <text class="axis-label" x="108" y="281">0.70</text>
    <text class="axis-label" x="108" y="326">0.60</text>
    <text class="axis-label" x="108" y="371">0.50</text>
    <text class="axis-label" x="108" y="416">0.40</text>
    <text class="axis-label" x="108" y="461">0.30</text>
    <text class="axis-label" x="108" y="506">0.20</text>
    <text class="axis-label" x="108" y="551">0.10</text>
    <text class="axis-label" x="108" y="596">0.00</text>
  </g>

  <!-- connectors -->
  <g class="connectors" fill="url(#link-fill)">
    <polygon points="172,169 250,208 250,226 172,186"/>
    <polygon points="172,210 250,241 250,258 172,227"/>
    <polygon points="172,251 250,276 250,292 172,268"/>
    <polygon points="172,292 250,311 250,327 172,309"/>
    <polygon points="172,333 250,345 250,361 172,350"/>
    <polygon points="172,377 250,380 250,394 172,394"/>
    <polygon points="172,426 250,413 250,429 172,443"/>
    <polygon points="172,467 250,449 250,463 172,484"/>
    <polygon points="172,508 250,482 250,497 172,525"/>
    <polygon points="172,549 250,515 250,531 172,566"/>
    <polygon points="172,590 250,551 250,565 172,607"/>
  </g>

  <!-- bars -->
  <g class="bars">
    <rect x="255" y="208" width="455" height="18" fill="var(--bar-1)"/>
    <text class="bar-label bar-label--lg" x="270" y="221">SALES – SPECIFIC MULTI – MEASUREMENT ASSESSMENT</text>

    <rect x="255" y="241" width="373" height="17" fill="var(--bar-2)"/>
    <text class="bar-label bar-label--lg" x="270" y="253.5">MULTI – MEASUREMENT ASSESSMENT</text>

    <rect x="255" y="276" width="308" height="16" fill="var(--bar-3)"/>
    <text class="bar-label" x="270" y="287" style="font-size:8.5px">HIGHLY STRUCTURED INTERVIEW WITH SCORECARD</text>

    <rect x="255" y="311" width="255" height="16" fill="var(--bar-4)"/>
    <text class="bar-label bar-label--lg" x="270" y="323">GENERAL MENTAL ABILITY</text>

    <rect x="255" y="345" width="163" height="16" fill="var(--bar-5)"/>
    <text class="bar-label bar-label--lg" x="270" y="357">SKILLS TEST</text>

    <rect x="255" y="380" width="130" height="14" fill="var(--bar-6)"/>
    <text class="bar-label bar-label--sm" x="266" y="390">EMOTIONAL INTELLEGENCE</text>

    <rect x="255" y="413" width="130" height="16" fill="var(--bar-7)"/>
    <text class="bar-label" x="268" y="425" style="font-size:9px">REFERENCE CHECK</text>

    <rect x="255" y="449" width="108" height="14" fill="var(--bar-8)"/>
    <text class="bar-label bar-label--sm" x="263" y="459">TRADITIONAL INTERVIEW</text>

    <rect x="255" y="482" width="108" height="15" fill="var(--bar-9)"/>
    <text class="bar-label bar-label--sm" x="280" y="488" style="font-size:5.5px">BEHAVIOR OR</text>
    <text class="bar-label bar-label--sm" x="262" y="495" style="font-size:5.5px">PERSONALITY TEST</text>

    <rect x="255" y="515" width="102" height="16" fill="var(--bar-10)"/>
    <text class="bar-label bar-label--lg" x="270" y="527">RESUME</text>

    <rect x="255" y="551" width="78" height="14" fill="var(--bar-11)"/>
    <text class="bar-label bar-label--sm" x="264" y="561">CULTUR E TEST</text>
  </g>

  <!-- value tags -->
  <g class="tags">
    <polygon class="tag" points="706,201 736,201 742,214 706,214"/>
    <text class="tag-text tag-text--lg" x="712" y="211">91 %</text>
    <polygon class="tag" points="624,234 654,234 660,247 624,247"/>
    <text class="tag-text tag-text--lg" x="630" y="244">71 %</text>
    <polygon class="tag" points="559,268 589,268 595,281 559,281"/>
    <text class="tag-text tag-text--lg" x="565" y="278">57 %</text>
    <polygon class="tag" points="506,303 536,303 542,316 506,316"/>
    <text class="tag-text tag-text--lg" x="512" y="313">51 %</text>
    <polygon class="tag" points="414,337 444,337 450,350 414,350"/>
    <text class="tag-text tag-text--lg" x="420" y="347">33 %</text>
    <polygon class="tag" points="381,373 407,373 413,384 381,384"/>
    <text class="tag-text tag-text--sm" x="387" y="381">23 %</text>
    <polygon class="tag" points="381,405 411,405 417,418 381,418"/>
    <text class="tag-text tag-text--lg" x="387" y="415">23 %</text>
    <polygon class="tag" points="359,442 385,442 391,453 359,453"/>
    <text class="tag-text tag-text--sm" x="365" y="450">20 %</text>
    <polygon class="tag" points="359,475 385,475 391,486 359,486"/>
    <text class="tag-text tag-text--sm" x="365" y="483">20 %</text>
    <polygon class="tag" points="353,508 383,508 389,521 353,521"/>
    <text class="tag-text tag-text--lg" x="359" y="518">18 %</text>
    <polygon class="tag" points="329,544 355,544 361,555 329,555"/>
    <text class="tag-text tag-text--sm" x="335" y="552">13 %</text>
  </g>

  <!-- client name beside top method -->
  <text class="client-name" x="752" y="213">Vex Pim ORA</text>

  <!-- horizontal axis title -->
  <path class="footer-band" d="M565,627 Q585,577 610,577 L898,577 L898,627 Z"/>
  <text class="footer-title" x="613" y="611">HIRING METHOD</text>
</svg>
</body>
</html>
```